website for local kavenda practicioner and yoga teacher trainer

The website should function primarily as:
A place where people can discover Kavenda and book sessions.
A central hub connecting all of my work.
A professional home that reflects my personality and approach.
Website design for Liesbet Oonwerk — Kavenda® Structural Integration practitioner, movement educator, yoga teacher and teacher trainer.
A website that can grow with future projects.
The website should feel: Warm, Human, Invitational, Professional, Accessible, Intelligent, Calm, Clear, Playful, Exploratory, Trustworthy
Avoid: New age aesthetics, Mystical clichés, Excessive spirituality, ”Guru" vibes, Overly clinical design, Corporate wellness branding, Busy layouts
Think: modern, grounded, curious and real.
My work combines three interconnected areas:
1.Bodywork: Touch, structure, awareness and one-on-one support.
2. Movement: Yoga, Pilates and embodied movement.
3. Education: Teacher trainings, workshops and continued learning.
Underlying values:
Curiosity over certainty
Possibility over perfection
Complexity without overwhelm
Science and lived experience together
Exploration rather than dogma
Human beings before methods
The primary goal of the website is to introduce people to Kavenda® Structural Integration and make it easy for them to:
Understand what Kavenda is
Discover whether it might be relevant for them
Learn what to expect from a session
Book an appointment
Booking should always feel visible and easy.
Secondary Goal: Present all other aspects of my work in one coherent place:
Yoga classes
Pilates classes
Teacher trainings
Workshops
Retreats
One-on-one movement sessions
Collaborations with studios
Website Structure
1: HOME
1.1.Hero Section: Large welcoming image
1.2 Two Main Pathways
- Bodywork: Kavenda® Structural Integration
- Movement & Education: Yoga, Pilates, trainings, workshops and retreats
- About Preview: Small introduction with portrait. + Button:
Read More
1.3 Current Events / What's Coming Up: Upcoming trainings, workshops and retreats. (This section should be easy to update)
1.4. Contact / Newsletter: Simple contact information
2: Kavenda® Structural Integration
What is Kavenda?
For whom is it?
What does a session look like?
FAQ
Prices
Booking
Future possibility:
Kaven Movement sessions
3: Movement
- Introductory text.
- Studio Classes (link to “my home base” - > local yoga studio)
- One-to-One Sessions: booking option (this is small; not a key aspect I want to promote)
- Workshops/ Retreats / Teacher Trainings => This section should be flexible and easy to update. Visitors should be able to click into specific offerings.
4. Events
Dynamic page for: Teacher trainings, Retreats, Workshops (see section in movement; here more elaborate)
Each event should contain: Image, Short description, Location, Date, Button for more information. (Linking to hosting studio/location)
5. Work With Me
For studios, organisations and teacher training schools.
Examples: Guest teaching, Workshops, Anatomy, Sequencing, Teacher development , Continuing education -> Clear call-to-action.
Call to action!!=> Book a Session
Prominent button in the navigation.
Footer:
- About Me: Longer biography (6th page)
Personal story and background.
- Testimonials (7th page): Separate page containing testimonials from:
Kavenda clients
Students
Teacher trainees
- Contact: 8th page
Visual Direction
Natural textures. Lots of white space.Editorial feeling.Professional photography.Simple navigation.
Less "wellness influencer.” More:Thoughtful, Contemporary, Timeless, Grounded, Human
Photography should show:
Teaching
Hands-on work
Natural movement
Real interaction
Simplicity
Avoid stereotypical yoga imagery and overly spiritual aesthetics.
Keywords
Warm. Curious. Human. Professional. Embodied. Intelligent. Accessible. Playful. Grounded. Exploratory. Real.
Inspiration / Core Message
Helping people feel more at home in their bodies through touch, movement and education.
The website should communicate that these are not separate services, but different expressions of the same intention:
Bodywork • Movement • Education.
Colours:
light orange/beige: e3d5c4
light orange/off white: f9f7f3
gray azure: 556b78
orange: d07b5a
grey orange: c09f80
dark grey: 3e3e3e
dark gray cyan 2f4f4f
gray green colour: a7c4a0
Fonts: Montserrat and Poppins + raleway
In added documents a try out idea of a website + logo. I will mainly use the logo with diffrent colours (image next to text).
My audience consists of people who want to feel more at home in their bodies and who appreciate a thoughtful, grounded and human approach to movement, touch and education. (30-65yo)
wellbeing
5+ page
- montserrat, poppins, raleway

```html
<!DOCTYPE html>
<html lang="en">
<head>
<meta charset="utf-8">
<title>Liesbet Oonwerk — Kavenda® Structural Integration</title>
<link href="https://fonts.googleapis.com/css2?family=Montserrat:wght@400;500;600;700&family=Poppins:wght@400;500&display=swap" rel="stylesheet">
<style>
:root{
  --sand:#e3d5c4;
  --offwhite:#f9f7f3;
  --azure:#556b78;
  --orange:#d07b5a;
  --greyorange:#c09f80;
  --dark:#3e3e3e;
  --cream:#f6efe7;
  --pill:#f4f0ea;
  --text:#6b6b6b;
}
*{box-sizing:border-box;margin:0;padding:0}
html,body{width:1200px;height:5115px;overflow:hidden}
body{position:relative;background:#fff;font-family:"Montserrat",sans-serif;color:var(--text)}
.abs{position:absolute}
a{color:inherit;text-decoration:none}
.btn{position:absolute;display:flex;align-items:center;justify-content:center;font:600 15px "Montserrat",sans-serif;border-radius:3px}
.btn-sand{background:var(--sand);color:var(--orange);box-shadow:0 2px 4px rgba(0,0,0,.12)}
.h-section{position:absolute;left:0;width:1200px;text-align:center;font:500 46px/1.25 "Montserrat",sans-serif;color:var(--orange)}
.h-block{font:500 30px/1.08 "Montserrat",sans-serif;color:var(--azure)}
.para{font:400 16px/1.42 "Montserrat",sans-serif;color:var(--text)}
/* nav */
.nav-logo{left:107px;top:30px;display:flex;align-items:center;gap:10px;font:500 18px "Montserrat",sans-serif;color:var(--dark)}
.nav-logo span.dot{width:22px;height:22px;border-radius:50%;background:var(--dark)}
.nav-links{top:38px;left:330px;display:flex;gap:32px;font:500 14px "Poppins",sans-serif;color:var(--dark)}
.nav-links .active{color:var(--orange)}
.nav-phone{left:795px;top:32px;display:flex;align-items:center;gap:10px;font:500 15px "Poppins",sans-serif;color:var(--orange)}
.nav-phone .ic{width:28px;height:28px;border-radius:50%;background:var(--orange);display:flex;align-items:center;justify-content:center}
/* hero */
.hero-photo{left:0;top:0;width:1200px;height:680px;background:linear-gradient(100deg,#f7f4ef 0%,#efe9e1 45%,#e6ddd2 70%,#f2ede6 100%)}
.hero-title{left:103px;top:222px;font:500 60px/1.1 "Montserrat",sans-serif;color:var(--orange)}
.hero-text{left:108px;top:370px;width:430px;font:400 16.5px/1.35 "Montserrat",sans-serif;color:var(--dark)}
.btn-hero{left:107px;top:466px;width:216px;height:47px;background:var(--azure);color:#fff;font-size:14.5px}
/* pathways */
.img-ph{position:absolute}
.pill{position:absolute;width:220px;height:355px;border-radius:110px;background:var(--pill)}
.pill .art{position:absolute;left:55px;top:55px;width:110px;height:110px;border-radius:50%;background:#f1d9cc}
.pill .lbl{position:absolute;left:0;width:220px;text-align:center;top:235px;font:500 25px "Montserrat",sans-serif;color:var(--azure)}
/* events */
.card-img{position:absolute;top:3460px;width:310px;height:248px;border-radius:18px}
.card-date{position:absolute;top:3738px;font:500 19px "Montserrat",sans-serif;color:var(--orange)}
.card-title{position:absolute;top:3768px;width:310px;font:600 20px/1.5 "Montserrat",sans-serif;color:var(--azure)}
.arrow{position:absolute;top:3662px;width:26px;height:26px;border-radius:50%;display:flex;align-items:center;justify-content:center}
/* subscribe */
.contact-lbl{font:600 14px "Montserrat",sans-serif;color:var(--orange);text-transform:uppercase}
.contact-val{font:400 14px/1.4 "Montserrat",sans-serif;color:var(--dark)}
/* footer */
.f-head{font:600 16px "Montserrat",sans-serif;color:#fff}
.f-text{font:400 14px/1.5 "Montserrat",sans-serif;color:#e8e8e8}
.field{position:absolute;left:805px;width:268px;border-bottom:1px solid rgba(255,255,255,.35);padding-bottom:12px;font:400 14px "Montserrat",sans-serif;color:#fff}
</style>
</head>
<body>

<!-- HERO -->
<div class="abs hero-photo" role="img" aria-label="Practitioner guiding a client's posture in a bright studio"></div>
<svg class="abs" style="left:0;top:560px" width="1200" height="140" viewBox="0 0 1200 140">
  <path d="M0 95 C260 125 430 118 640 70 C860 20 1020 25 1200 45 L1200 140 L0 140 Z" fill="#fff"/>
  <path d="M0 95 C260 125 430 118 640 70 C860 20 1020 25 1200 45" fill="none" stroke="var(--orange)" stroke-width="7"/>
</svg>

<header>
  <div class="abs nav-logo"><span class="dot"></span>Liesbet Oonwerk</div>
  <nav class="abs nav-links">
    <a class="active">Home</a><a>Kavenda®</a><a>Movement</a><a>Events</a><a>Work With Me</a>
  </nav>
  <div class="abs nav-phone"><span class="ic"><svg width="14" height="14" viewBox="0 0 24 24"><path fill="#fff" d="M6.6 10.8a15 15 0 0 0 6.6 6.6l2.2-2.2c.3-.3.7-.4 1-.2 1.1.4 2.3.6 3.6.6.6 0 1 .4 1 1V20c0 .6-.4 1-1 1A17 17 0 0 1 3 4c0-.6.4-1 1-1h3.5c.6 0 1 .4 1 1 0 1.3.2 2.5.6 3.6.1.3 0 .7-.2 1z"/></svg></span>555-201-847</div>
  <a class="btn btn-sand" style="left:935px;top:24px;width:155px;height:46px">Book Sessions</a>
</header>

<section>
  <h1 class="abs hero-title">Local Kavenda<br>Practicioner</h1>
  <p class="abs hero-text">I offer group classes,training,retreats ,and one-on-oe sessions in movement and bodywork both locally and abroad.</p>
  <a class="btn btn-hero">Book an appointment</a>
</section>

<!-- PATHWAYS -->
<section>
  <h2 class="h-section" style="top:722px">Two Main Pathways</h2>
  <svg class="abs" style="left:380px;top:800px" width="500" height="700" viewBox="0 0 500 700">
    <path d="M20 140 C120 60 200 30 250 10" fill="none" stroke="#efd6cb" stroke-width="1.5"/>
    <path d="M40 400 C160 480 320 560 480 660" fill="none" stroke="#efd6cb" stroke-width="1.5"/>
  </svg>
  <div class="img-ph" style="left:107px;top:873px;width:312px;height:482px;border-radius:156px;background:linear-gradient(160deg,#ece6df,#d9cfc6 60%,#4a4a4a 100%)" role="img" aria-label="Teacher assisting a student in a balancing pose"></div>
  <div class="img-ph" style="left:402px;top:928px;width:128px;height:165px;border-radius:64px;background:linear-gradient(160deg,#f0ebe4,#d8cdc2)" role="img" aria-label="Students practising standing poses in class"></div>
  <h3 class="abs h-block" style="left:610px;top:918px">Bodywork:<br>Kavenda®<br>Structural Integration</h3>
  <p class="abs para" style="left:612px;top:1030px;width:430px">Lorem Ipsum generators on the Internet tend to repeat predefined chunks as necessary, making this the first true generator on the Internet. It uses a dictionary of over 200 Latin words, combined with a handful of model sentence structures, to generate Lorem Ipsum which looks reasonable. The generated Lorem Ipsum is therefore always free from repetition, injected humour, or non-characteristic words etc.</p>
  <a class="btn btn-sand" style="left:612px;top:1265px;width:155px;height:46px">Read More</a>

  <h3 class="abs h-block" style="left:105px;top:1475px">Movement &amp;<br>Education</h3>
  <p class="abs para" style="left:105px;top:1558px;width:440px">Lorem Ipsum generators on the Internet tend to repeat predefined chunks as necessary, making this the first true generator on the Internet. It uses a dictionary of over 200 Latin words, combined with a handful of model sentence structures, to generate Lorem Ipsum which looks reasonable.</p>
  <a class="btn btn-sand" style="left:105px;top:1738px;width:155px;height:47px">Read More</a>
  <div class="img-ph" style="left:608px;top:1465px;width:482px;height:325px;border-radius:170px 160px 150px 180px;background:linear-gradient(180deg,#f2f2f0,#e6e4e0 70%,#3f6e8c 100%)" role="img" aria-label="Woman meditating cross-legged on a mat"></div>

  <svg class="abs" style="left:300px;top:1870px" width="400" height="40"><path d="M0 5 C120 20 260 25 400 30" fill="none" stroke="#efd6cb" stroke-width="1.5"/></svg>
  <div class="pill" style="left:107px;top:1835px"><div class="art" role="img" aria-label="Line drawing of a seated yoga pose"></div><div class="lbl">Yoga</div></div>
  <div class="pill" style="left:365px;top:1910px"><div class="art" role="img" aria-label="Line drawing of a downward dog pose"></div><div class="lbl">Pilates</div></div>
  <div class="pill" style="left:622px;top:1835px"><div class="art" role="img" aria-label="Line drawing of a backbend pose"></div><div class="lbl">Trainings</div></div>
  <div class="pill" style="left:878px;top:1910px"><div class="art" role="img" aria-label="Line drawing of a warrior pose"></div><div class="lbl">Workshops</div></div>
</section>

<!-- ABOUT -->
<section>
  <div class="img-ph" style="left:0;top:2335px;width:1200px;height:840px;background:linear-gradient(180deg,#fbfaf8 0%,#f1ece6 35%,#c5b39f 70%,#a68f7a 100%)" role="img" aria-label="Woman in a cobra pose on a mat in a sunlit room"></div>
  <svg class="abs" style="left:0;top:3100px" width="1200" height="110" viewBox="0 0 1200 110">
    <path d="M0 65 C220 95 420 95 640 55 C860 15 1020 10 1200 25 L1200 110 L0 110 Z" fill="#fff"/>
    <path d="M0 65 C220 95 420 95 640 55 C860 15 1020 10 1200 25" fill="none" stroke="var(--orange)" stroke-width="7"/>
  </svg>
  <h2 class="h-section" style="top:2390px">About Us</h2>
  <p class="abs para" style="left:250px;top:2468px;width:720px;text-align:center;font-size:15.5px">Lorem Ipsum generators on the Internet tend to repeat predefined chunks as necessary, making this the first true generator on the Internet. It uses a dictionary of over 200 Latin words, combined with a handful of model sentence structures, to generate Lorem Ipsum which looks reasonable.</p>
  <a class="btn btn-sand" style="left:522px;top:2585px;width:156px;height:46px">Read More</a>
</section>

<!-- EVENTS -->
<section>
  <h2 class="h-section" style="top:3282px">Upcoming Trainings, Workshops<br>And Retreats</h2>
  <div class="arrow" style="left:57px;background:var(--sand)"><svg width="10" height="10" viewBox="0 0 10 10"><path d="M6.5 1.5 3 5l3.5 3.5" fill="none" stroke="var(--greyorange)" stroke-width="1.6"/></svg></div>
  <div class="arrow" style="left:1115px;background:#b24d22"><svg width="10" height="10" viewBox="0 0 10 10"><path d="M3.5 1.5 7 5 3.5 8.5" fill="none" stroke="#fff" stroke-width="1.6"/></svg></div>

  <div class="card-img" style="left:105px;background:linear-gradient(160deg,#f3f1ee,#d8d3cc 70%,#d99a63)" role="img" aria-label="Group doing side stretches on mats"></div>
  <div class="card-date" style="left:105px">JUNE 17, 2026</div>
  <div class="card-title" style="left:105px">Lorem Ipsum generators on the Internet tend</div>
  <a class="btn btn-sand" style="left:107px;top:3842px;width:155px;height:46px">Read More</a>

  <div class="card-img" style="left:445px;background:linear-gradient(160deg,#f4f2ef,#e1d6cb 60%,#b9a894)" role="img" aria-label="Practitioner working on a client's leg"></div>
  <div class="card-date" style="left:445px">JUNE 17, 2026</div>
  <div class="card-title" style="left:445px">Lorem Ipsum generators on the Internet tend</div>
  <a class="btn btn-sand" style="left:446px;top:3842px;width:155px;height:46px">Read More</a>

  <div class="card-img" style="left:785px;background:linear-gradient(160deg,#a9c4bf,#c8b9a8 55%,#7fb3ad)" role="img" aria-label="Students resting on mats outdoors"></div>
  <div class="card-date" style="left:785px">JUNE 17, 2026</div>
  <div class="card-title" style="left:785px">Lorem Ipsum generators on the Internet tend</div>
  <a class="btn btn-sand" style="left:785px;top:3842px;width:155px;height:46px">Read More</a>
</section>

<!-- SUBSCRIBE -->
<section>
  <div class="abs" style="left:0;top:4020px;width:1200px;height:560px;background:var(--cream)"></div>
  <h2 class="abs" style="left:105px;top:4120px;font:500 46px/1.25 'Montserrat',sans-serif;color:var(--orange)">Subscribe for Yoga<br>Tips and Inspiration</h2>
  <div class="abs" style="left:105px;top:4250px;width:508px;height:62px;background:#fff;box-shadow:0 2px 6px rgba(0,0,0,.06)"></div>
  <div class="abs" style="left:130px;top:4272px;font:400 15px 'Montserrat',sans-serif;color:#777">Enter Mail ID</div>
  <a class="btn btn-sand" style="left:450px;top:4260px;width:148px;height:42px;font-size:14px;box-shadow:none">Subscribe</a>
  <div class="abs" style="left:105px;top:4348px"><div class="contact-lbl">Call Us</div><div class="contact-val">(0) - 0555-310-472</div></div>
  <div class="abs" style="left:280px;top:4348px"><div class="contact-lbl">Mail Us</div><div class="contact-val">hello@oonwerkstudio.com</div></div>
  <div class="abs" style="left:492px;top:4345px"><div class="contact-lbl">Location</div><div class="contact-val">48 Meadow Lane QX4 7RT<br>United Kingdom</div></div>
  <div class="img-ph" style="left:705px;top:4085px;width:445px;height:445px;border-radius:50%;background:linear-gradient(150deg,#efe6dc,#e9c7cf 50%,#3f4a4f 85%,#5aa9a0)" role="img" aria-label="Therapist using a massage tool on a client's leg"></div>
</section>

<!-- FOOTER -->
<footer>
  <svg class="abs" style="left:0;top:4470px" width="1200" height="645" viewBox="0 0 1200 645">
    <path d="M0 40 C220 80 430 90 640 75 C860 60 1020 90 1200 60 L1200 645 L0 645 Z" fill="var(--dark)"/>
    <path d="M0 40 C220 80 430 90 640 75 C860 60 1020 90 1200 60" fill="none" stroke="var(--orange)" stroke-width="7"/>
  </svg>

  <div class="abs f-head" style="left:107px;top:4680px">ABOUT ME</div>
  <p class="abs f-text" style="left:107px;top:4718px;width:270px;font-size:13.5px">Lorem Ipsum generators on the Internet tend to repeat predefined chunks as necessary,</p>
  <a class="abs" style="left:107px;top:4780px;font:600 14px 'Montserrat',sans-serif;color:var(--orange);text-decoration:underline">Read More</a>
  <div class="abs" style="left:107px;top:4890px;display:flex;align-items:center;gap:10px;font:500 22px 'Montserrat',sans-serif;color:#fff"><span style="width:26px;height:26px;border-radius:50%;background:#fff;display:block"></span>Liesbet Oonwerk</div>
  <p class="abs f-text" style="left:105px;top:4958px;font-size:13.5px;line-height:1.45;color:var(--orange)">Copyright © 2026. <span style="color:#fff">LiesbetOonwerk ,</span><br>All rights reserved</p>
  <div class="abs f-text" style="left:105px;top:5002px;font-size:13.5px">Privacy Policy &nbsp; I &nbsp; Term's &amp; Condition</div>
  <div class="abs" style="left:105px;top:5030px;display:flex;gap:12px">
    <span style="width:16px;height:16px;border-radius:50%;background:#fff"></span>
    <span style="width:16px;height:16px;border-radius:50%;background:#fff"></span>
    <span style="width:16px;height:16px;border-radius:50%;background:#fff"></span>
  </div>

  <div class="abs f-head" style="left:442px;top:4675px">TESTIMONIALS</div>
  <p class="abs f-text" style="left:442px;top:4722px;width:285px;font-size:13.5px">"Lorem Ipsum generators on the Internet tend to repeat predefined chunks as necessary, making this the first true generator on the Internet. "</p>
  <div class="img-ph" style="left:442px;top:4862px;width:46px;height:46px;border-radius:50%;background:linear-gradient(160deg,#e8dccd,#b69a82)" role="img" aria-label="Client portrait"></div>
  <div class="abs" style="left:500px;top:4866px;font:600 14px 'Montserrat',sans-serif;color:#fff">Anna Verbeek</div>
  <div class="abs" style="left:500px;top:4886px;font:italic 400 13px 'Montserrat',sans-serif;color:#ddd">Kavenda clients</div>
  <div class="abs" style="left:442px;top:4932px;display:flex;gap:8px">
    <span style="width:6px;height:6px;border-radius:50%;background:var(--orange)"></span>
    <span style="width:6px;height:6px;border-radius:50%;background:#5a5a5a"></span>
    <span style="width:6px;height:6px;border-radius:50%;background:#5a5a5a"></span>
  </div>
  <a class="abs" style="left:442px;top:4962px;font:500 14px 'Montserrat',sans-serif;color:var(--orange);text-decoration:underline">View All</a>

  <div class="abs" style="left:785px;top:4640px;width:307px;height:415px;background:var(--azure);border-radius:18px 18px 0 0;overflow:hidden">
    <div style="height:92px;background:var(--orange);padding:30px 20px 0">
      <div style="font:600 16px 'Montserrat',sans-serif;color:#fff">CONTACT US</div>
      <div style="font:400 14px 'Montserrat',sans-serif;color:#fbe3d8;margin-top:4px">We are here to help you</div>
    </div>
  </div>
  <div class="field" style="top:4762px">Your Name</div>
  <div class="field" style="top:4812px">Your Email</div>
  <div class="field" style="top:4862px">Your Phone</div>
  <div class="field" style="top:4912px;padding-bottom:52px">Your Comment</div>
  <a class="btn btn-sand" style="left:805px;top:4998px;width:155px;height:47px">Submit Now</a>
</footer>

</body>
</html>
```